Flyer für Sternenhimmel-Beobachtungen
Zielgruppe
Mit Lumo Vale biete ich geführte Sternenhimmel-Beobachtungen in Hönow (Hoppegarten) an.
Die Teilnehmer erhalten interessante Informationen über den aktuellen Sternenhimmel, astronomische Ereignisse und besondere Himmelsobjekte.
Mit einem großen Teleskop und Ferngläsern beobachten wir Objekte unseres Sonnensystems sowie Sterne, Doppelsterne, Sternhaufen, Nebel und Galaxien.
Je nach Jahreszeit dauern die Touren zwischen 1 und 2 Stunden.
Ausrüstung, Stühle, Decken, Snacks und Tee werden von mir bereitgestellt.
Aufgabenstellung
Gerne maximal 2 Seiten. Mit Informationen auf Vorderseite und Rückseite.

```html
<!DOCTYPE html>
<html lang="de">
<head>
<meta charset="utf-8">
<title>Lumo Vale – Flyer</title>
<link rel="stylesheet" href="https://fonts.googleapis.com/css2?family=Lato:wght@400;700;900&display=swap">
<style>
:root{
  --bg:#a9dde2;
  --bg-light:#e6f5f5;
  --ink-dark:#0a2b2a;
  --panel-dark:#0c302f;
  --panel-mid:#17504e;
  --accent:#6cc4ca;
  --accent-text:#74d0d5;
  --white:#f2f7f7;
  --muted:#d6e6e6;
}
*{box-sizing:border-box;margin:0;padding:0}
html,body{width:882px;height:1200px;overflow:hidden}
body{
  font-family:'Lato',sans-serif;
  background:linear-gradient(180deg,var(--bg) 0%,var(--bg) 55%,var(--bg-light) 100%);
  position:relative;
}
.page{
  position:absolute;top:313px;width:410px;height:574px;overflow:hidden;
  background:var(--panel-dark);
  box-shadow:0 6px 20px rgba(0,40,45,.18);
}
.page--front{left:20px}
.page--back{left:452px}
.abs{position:absolute}

.url-tab{
  position:absolute;height:22px;width:160px;background:var(--accent);
  color:var(--ink-dark);font-size:8.5px;display:flex;align-items:center;
}
.page--front .url-tab{top:25px;left:0;border-radius:0 11px 11px 0;padding-left:46px}
.page--back .url-tab{top:444px;right:0;border-radius:11px 0 0 11px;padding-left:46px}

.hero-photo{
  position:absolute;left:0;top:40px;width:410px;height:260px;
  background:linear-gradient(180deg,#12302f 0%,#2c4a4e 40%,#5a5e64 70%,#3a3f44 85%,#0d1d1f 100%);
}
.brand{
  position:absolute;display:flex;align-items:center;gap:7px;
  color:var(--white);font-weight:900;
}
.brand__dot{width:12px;height:12px;border-radius:50%;background:var(--white);flex:none}
.page--front .brand{top:98px;left:232px;font-size:22px}
.page--back .brand{top:70px;left:268px;font-size:16px}

.curve{position:absolute;left:0;top:0;width:410px;height:574px}

.headline{position:absolute;font-size:31px;line-height:31px;letter-spacing:-.2px}
.headline__soft{color:var(--accent-text);font-weight:400;display:block}
.headline__bold{color:var(--white);font-weight:700;display:block}
.page--front .headline{left:58px;top:283px}
.page--back .headline{left:37px;top:75px}

.copy{position:absolute;color:var(--muted);font-size:8.6px;line-height:11.3px}
.copy p+p{margin-top:11px}
.copy b{color:var(--white);font-weight:700}
.page--front .copy{left:58px;top:393px;width:290px}
.page--back .copy--intro{left:37px;top:191px;width:270px}

.guide-photo{
  position:absolute;left:42px;top:302px;width:103px;height:157px;border-radius:26px;
  background:linear-gradient(180deg,#6f8a70 0%,#9aa89a 35%,#2a2d31 60%,#1c1f22 100%);
}
.guide-title{position:absolute;left:169px;top:328px;font-size:15px;color:var(--accent-text)}
.guide-title b{color:var(--white)}
.page--back .copy--guide{left:169px;top:358px;width:215px}

.band{
  position:absolute;left:0;top:482px;width:410px;height:92px;background:var(--accent);
  color:var(--ink-dark);
}
.page--front .band{border-top-right-radius:34px;display:flex;align-items:center;justify-content:center;text-align:center;font-size:15px;line-height:20px}
.page--front .band b{font-weight:700}
.page--back .band{border-top-left-radius:34px}
.band__note{position:absolute;left:50px;top:20px;width:150px;text-align:center;font-size:9.5px;line-height:12px}
.band__contact{position:absolute;left:228px;top:16px;font-size:15px;font-weight:700;line-height:21px}
</style>
</head>
<body>

<section class="page page--front">
  <div class="hero-photo" role="img" aria-label="Foto: Silhouette eines Mannes am Teleskop in der Abenddämmerung"></div>
  <svg class="curve" viewBox="0 0 410 574" aria-hidden="true">
    <defs>
      <linearGradient id="frontFade" x1="0" y1="0" x2="0" y2="1">
        <stop offset="0" stop-color="#17504e"/>
        <stop offset=".35" stop-color="#0f3a39"/>
        <stop offset="1" stop-color="#0a2b2a"/>
      </linearGradient>
    </defs>
    <path d="M0 300 C90 255 300 248 410 292 L410 574 L0 574 Z" fill="url(#frontFade)"/>
  </svg>
  <div class="url-tab">www.lumo-vale.de</div>
  <div class="brand"><span class="brand__dot"></span>Lumo Vale</div>
  <h1 class="headline">
    <span class="headline__soft">Entdecke den</span>
    <span class="headline__soft">Sternenhimmel</span>
    <span class="headline__bold">hautnah &amp; geführt!</span>
  </h1>
  <div class="copy">
    <p>Erlebe mit <b>Lumo Vale – Jonas’ Guided Stargazing</b> unvergessliche Nächte unter dem funkelnden Himmel von Berlin &amp; Brandenburg!</p>
    <p>Begib dich mit Jonas Albrecht, leidenschaftlichem Astronomie-Enthusiasten seit Kindertagen, auf eine faszinierende Reise zu den Geheimnissen des Universums.</p>
  </div>
  <div class="band"><p><b>Komm mit auf eine Reise zu den Wundern<br>des Kosmos</b> – ich freue mich darauf!</p></div>
</section>

<section class="page page--back">
  <svg class="curve" viewBox="0 0 410 574" aria-hidden="true">
    <defs>
      <linearGradient id="backTop" x1="0" y1="0" x2="1" y2="1">
        <stop offset="0" stop-color="#0e3534"/>
        <stop offset="1" stop-color="#1d5856"/>
      </linearGradient>
    </defs>
    <path d="M0 0 L410 0 L410 108 C330 170 160 200 0 205 Z" fill="url(#backTop)"/>
  </svg>
  <div class="brand"><span class="brand__dot"></span>Lumo Vale</div>
  <h2 class="headline">
    <span class="headline__soft">Erlebe das</span>
    <span class="headline__soft">Universum mit</span>
    <span class="headline__bold">eigenen Augen</span>
  </h2>
  <div class="copy copy--intro">
    <p>Auf den geführten Touren erfährst du spannende Mythen aus der griechischen Antike, lernst die Sternbilder neu kennen und entdeckst beeindruckende Himmelsobjekte – von den Planeten unseres Sonnensystems bis hin zu weit entfernten Galaxien.</p>
    <p>Ausgestattet mit leistungsstarkem Teleskop und hochwertigen Ferngläsern tauchst du ein in Sternhaufen, leuchtende Nebel und spektakuläre Supernova-Überreste.</p>
  </div>
  <div class="guide-photo" role="img" aria-label="Porträtfoto des Guides mit Teleskop im Freien"></div>
  <h3 class="guide-title">Dein <b>Guide</b></h3>
  <div class="copy copy--guide">
    <p>Ich bin <b>Jonas Albrecht</b>, leidenschaftlicher Sternenbeobachter seit meiner Kindheit. Mit Lumo Vale – Jonas’ Guided Stargazing möchte ich meine Begeisterung teilen und dir den Nachthimmel über Berlin &amp; Brandenburg näherbringen.</p>
  </div>
  <div class="url-tab">www.lumo-vale.de</div>
  <div class="band">
    <p class="band__note">Für Fragen oder erste Anfragen stehe ich dir jederzeit gern zur Verfügung.</p>
    <p class="band__contact">jonas@lumo-vale.de<br>+49 160 5550142</p>
  </div>
</section>

</body>
</html>
```